Corvane Business Cards & Staionary
Corvane, Inc.
Project: Corvane Business Cards & Staionary
Corvane Business Cards & Staionary - Real Estate
Creative Brief
Professional
Leonard T. Haskovich
President
418 W. Thornberry Blvd. Harlow Springs, TX 75460
len@corvanetx.com

```html
<!DOCTYPE html>
<html lang="en">
<head>
<meta charset="utf-8">
<title>Corvane, Inc. — Business Cards</title>
<link rel="stylesheet" href="https://fonts.googleapis.com/css2?family=Libre+Baskerville:wght@400;700&display=swap">
<style>
  :root {
    --backdrop: #e6e4e1;
    --card-black: #111111;
    --card-white: #fbfbfa;
    --gold: #d4a12a;
    --ink: #3b3b3b;
    --ink-soft: #6d6d6d;
    --paper-text: #ffffff;
  }
  * { box-sizing: border-box; margin: 0; padding: 0; }
  html, body {
    width: 1200px; height: 653px; overflow: hidden;
    background: var(--backdrop);
    font-family: "Libre Baskerville", Georgia, serif;
  }
  .sheet {
    width: 1200px; height: 653px;
    display: grid;
    grid-template-columns: 500px 500px;
    grid-template-rows: 286px 286px;
    gap: 27px 60px;
    padding: 27px 70px;
  }
  .card {
    position: relative; overflow: hidden;
    box-shadow: 0 6px 18px rgba(0,0,0,.22);
  }
  .card--black { background: var(--card-black); color: var(--paper-text); }
  .card--white { background: var(--card-white); color: var(--ink); }

  .brand {
    position: absolute; left: 0; right: 0;
    display: flex; flex-direction: column; align-items: center;
  }
  .brand__row { display: flex; align-items: center; gap: 12px; }
  .brand__square { width: 16px; height: 16px; background: var(--gold); }
  .brand__name { font-size: 34px; font-weight: 700; letter-spacing: .5px; white-space: nowrap; }
  .brand__tagline {
    margin-top: 8px; font-size: 8px; letter-spacing: 2px;
    text-transform: uppercase; color: var(--ink-soft);
  }
  .card--black .brand__tagline { color: #a9a9a9; }
  .card--front .brand { top: 108px; }
  .card--back .brand { top: 38px; }
  .card--back .brand__name { font-size: 24px; }

  .person { position: absolute; left: 0; right: 0; top: 118px; text-align: center; }
  .person__name { font-size: 18px; font-weight: 700; color: var(--gold); }
  .person__title { margin-top: 4px; font-size: 11px; color: var(--ink-soft); }
  .card--black .person__title { color: #bdbdbd; }
  .address {
    position: absolute; left: 0; right: 0; top: 182px;
    text-align: center; font-size: 11px; white-space: nowrap;
  }
  .contact-band {
    position: absolute; left: 0; right: 0; bottom: 0; height: 46px;
    background: var(--gold);
    display: flex; justify-content: center; align-items: center; gap: 28px;
    color: #ffffff; font-size: 11px; white-space: nowrap;
  }
  .contact-band__item { display: flex; align-items: center; gap: 6px; }
  .contact-band svg { width: 12px; height: 12px; fill: #ffffff; }
</style>
</head>
<body>
<main class="sheet">

  <article class="card card--black card--front">
    <div class="brand">
      <div class="brand__row"><span class="brand__square"></span><span class="brand__name">Corvane, Inc.</span></div>
      <p class="brand__tagline">Property Sales and Management</p>
    </div>
  </article>

  <article class="card card--white card--front">
    <div class="brand">
      <div class="brand__row"><span class="brand__square"></span><span class="brand__name">Corvane, Inc.</span></div>
      <p class="brand__tagline">Property Sales and Management</p>
    </div>
  </article>

  <article class="card card--black card--back">
    <div class="brand">
      <div class="brand__row"><span class="brand__square"></span><span class="brand__name">Corvane, Inc.</span></div>
      <p class="brand__tagline">Property Sales and Management</p>
    </div>
    <div class="person">
      <p class="person__name">Leonard T. Haskovich</p>
      <p class="person__title">President</p>
    </div>
    <p class="address">418 W. Thornberry Blvd. Harlow Springs, TX 75460</p>
    <div class="contact-band">
      <span class="contact-band__item"><svg viewBox="0 0 24 24"><path d="M6.6 10.8a15 15 0 0 0 6.6 6.6l2.2-2.2a1 1 0 0 1 1-.25 11.4 11.4 0 0 0 3.6.6 1 1 0 0 1 1 1V20a1 1 0 0 1-1 1A17 17 0 0 1 3 4a1 1 0 0 1 1-1h3.5a1 1 0 0 1 1 1c0 1.25.2 2.45.6 3.6a1 1 0 0 1-.25 1z"/></svg>(940) 555-0142</span>
      <span class="contact-band__item"><svg viewBox="0 0 24 24"><path d="M6.6 10.8a15 15 0 0 0 6.6 6.6l2.2-2.2a1 1 0 0 1 1-.25 11.4 11.4 0 0 0 3.6.6 1 1 0 0 1 1 1V20a1 1 0 0 1-1 1A17 17 0 0 1 3 4a1 1 0 0 1 1-1h3.5a1 1 0 0 1 1 1c0 1.25.2 2.45.6 3.6a1 1 0 0 1-.25 1z"/></svg>(940) 555-0187</span>
      <span class="contact-band__item"><svg viewBox="0 0 24 24"><path d="M2 5h20v14H2z M2 5l10 8 10-8" fill="none" stroke="#fff" stroke-width="2"/></svg>len@corvanetx.com</span>
    </div>
  </article>

  <article class="card card--white card--back">
    <div class="brand">
      <div class="brand__row"><span class="brand__square"></span><span class="brand__name">Corvane, Inc.</span></div>
      <p class="brand__tagline">Property Sales and Management</p>
    </div>
    <div class="person">
      <p class="person__name">Leonard T. Haskovich</p>
      <p class="person__title">President</p>
    </div>
    <p class="address">418 W. Thornberry Blvd. Harlow Springs, TX 75460</p>
    <div class="contact-band">
      <span class="contact-band__item"><svg viewBox="0 0 24 24"><path d="M6.6 10.8a15 15 0 0 0 6.6 6.6l2.2-2.2a1 1 0 0 1 1-.25 11.4 11.4 0 0 0 3.6.6 1 1 0 0 1 1 1V20a1 1 0 0 1-1 1A17 17 0 0 1 3 4a1 1 0 0 1 1-1h3.5a1 1 0 0 1 1 1c0 1.25.2 2.45.6 3.6a1 1 0 0 1-.25 1z"/></svg>(940) 555-0142</span>
      <span class="contact-band__item"><svg viewBox="0 0 24 24"><path d="M6.6 10.8a15 15 0 0 0 6.6 6.6l2.2-2.2a1 1 0 0 1 1-.25 11.4 11.4 0 0 0 3.6.6 1 1 0 0 1 1 1V20a1 1 0 0 1-1 1A17 17 0 0 1 3 4a1 1 0 0 1 1-1h3.5a1 1 0 0 1 1 1c0 1.25.2 2.45.6 3.6a1 1 0 0 1-.25 1z"/></svg>(940) 555-0187</span>
      <span class="contact-band__item"><svg viewBox="0 0 24 24"><path d="M2 5h20v14H2z M2 5l10 8 10-8" fill="none" stroke="#fff" stroke-width="2"/></svg>len@corvanetx.com</span>
    </div>
  </article>

</main>
</body>
</html>
```